Call for Papers for conference on VR/AR/MR for e-learning professionals, designers, & innovators

Create a main or "master" version of the Call for Papers for the oKTV2020 Conference along with variations of the master version for the nine Program Tracks. All versions should have the same
same layout and format, but use different color schemes and/or graphics so that they look like they are part of the same conference.

The design should:

1. consist of one ledger-sized page, edge-to-edge (no margins)
2. resonate with/reflect the conference theme (MOST IMPORTANT) -- future focus, clear vision, blurring of boundaries between physical and virtual;
3. be transcendent, vibrant, playful, fun, and futuristic, but not cliched;
4. prominently display the oKTV logo, PLUS the MostraqO logo, UQTA logo (under the text "Technically co-sponsored by") -- see the attached files. Where multiple versions of the logo have been supplied, you may select any version to use;
5. be able to be easily adapted by the Conference Track Chairs to create their own Calls for Papers and Proposals using the same layout and format, changing the color scheme and/or graphics to achieve differentiation from the main Call while ensuring it looks like it is part of the same conference.

Target Market(s)

Designers, Researchers, Technologists, and Business Professionals with an interest in using virtual reality (VR), augmented reality (AR), mixed reality (MR) and other XR technologies to support immersive learning in a range of education, training, and other settings.

Font styles to use
Sans Serif

Requirements
Must have
• Graphics and/or iconography, but NO PHOTOGRAPHS.
Should not have
• Photographs. Also please do not be too literal (e.g., while it is OK to include VR headsets they should not be a key feature of the design).

```html
<!DOCTYPE html>
<html lang="en">
<head>
<meta charset="utf-8">
<title>oKTV 2021 Call for Papers &amp; Proposals</title>
<link href="https://fonts.googleapis.com/css2?family=Montserrat:wght@300;400;500;600;700;800;900&display=swap" rel="stylesheet">
<style>
:root{
  --navy:#1f4b9e;
  --navy-deep:#23408f;
  --green:#1ba865;
  --green-soft:#2fb77a;
  --mint:#7bcf8c;
  --teal:#63c6b3;
  --sky:#2bb8ec;
  --band-a:#3a5aa8;
  --band-b:#2fb3e8;
  --ink:#222;
  --white:#fff;
}
*{margin:0;padding:0;box-sizing:border-box}
html,body{width:777px;height:1200px;overflow:hidden;background:var(--white)}
body{font-family:'Montserrat',sans-serif;color:var(--ink);position:relative}
.abs{position:absolute}

/* header */
.hero{left:0;top:0;width:777px;height:216px}
.hero svg{position:absolute;left:0;top:0}
.hero-title{left:34px;top:28px;font-weight:900;font-size:35px;line-height:41px;color:var(--navy-deep);letter-spacing:.3px}
.hero-sub{left:36px;top:114px;font-weight:700;font-size:15.5px;line-height:19px;color:var(--white)}
.hero-theme{left:35px;top:178px;font-size:9.4px;line-height:12px;color:var(--navy);font-weight:500}
.brand{left:468px;top:34px;display:flex;align-items:center;gap:8px}
.brand-dot{width:44px;height:44px;border-radius:50%;background:#3d8fd6}
.brand-name{font-weight:800;font-size:22px;line-height:22px;color:#1b7fd0;letter-spacing:-.2px}
.venue{right:38px;top:94px;text-align:right;font-weight:700;font-size:12.4px;line-height:15.5px;color:#111}
.topics{left:340px;top:141px;width:402px;text-align:right;font-size:9.6px;line-height:11.9px;color:var(--white);font-weight:400}

/* intro */
.intro{left:35px;top:226px;width:379px;font-size:9.55px;line-height:11.75px;text-align:justify;font-weight:400;color:#222}
.intro .note{margin-top:11px}
.intro .note b{color:var(--mint);font-weight:700}

/* streams */
.stream-tag{left:532px;top:243px;width:130px;height:23px;border-radius:12px;background:linear-gradient(90deg,var(--mint),var(--teal));color:var(--navy);font-weight:700;font-size:9.6px;line-height:23px;text-align:center}
.stream{left:452px;width:290px;border-radius:9px;background:linear-gradient(180deg,var(--green),var(--green-soft));color:var(--white);padding:6px 15px 7px;font-size:9.8px;line-height:11.8px}
.stream h3{font-size:10px;font-weight:700}
.stream ul{list-style:none}
.stream li{padding-left:9px;position:relative}
.stream li::before{content:"•";position:absolute;left:0}
.s1{top:274px;height:94px}
.s2{top:378px;height:84px}
.s3{top:472px;height:86px}

/* chevron panels */
.panel{color:var(--white)}
.panel h2{font-size:10.4px;font-weight:700;letter-spacing:.2px;margin-bottom:12px}
.panel p{font-size:9.55px;line-height:11.8px;text-align:justify}
.tracks{left:0;top:506px;width:400px;height:169px}
.tracks .inner{position:absolute;left:35px;top:18px;width:313px}
.review{left:0;top:681px;width:400px;height:168px}
.review .inner{position:absolute;left:35px;top:12px;width:313px}
.review p{margin:0}
.pub{left:369px;top:587px;width:408px;height:182px}
.pub .inner{position:absolute;left:48px;top:11px;width:325px}
.panel svg{position:absolute;left:0;top:0}

/* session format */
.fmt{left:35px;top:862px;width:344px}
.fmt h2{font-size:12.6px;font-weight:700;color:var(--navy);padding-bottom:5px;position:relative}
.fmt h2::after{content:"";position:absolute;left:0;bottom:-2px;width:64px;height:3px;background:var(--green)}
.fmt ul{list-style:none;margin-top:16px}
.fmt li{display:flex;gap:16px;font-size:9.8px;line-height:11.6px;text-align:justify;margin-bottom:9px}
.fmt li svg{flex:0 0 15px;margin-top:1px}
.fmt li b{color:var(--navy);font-weight:700}

/* dates */
.dates-title{left:490px;top:785px;width:180px;text-align:center;font-weight:700;font-size:9.8px;color:var(--navy)}
.dates-title::after{content:"";display:block;width:64px;height:3px;background:var(--green);margin:5px auto 0}
.dates{left:410px;top:811px;width:332px;list-style:none}
.dates li{display:flex;align-items:center;border-radius:5px;margin-bottom:4px;color:var(--white);min-height:18px;padding:2px 0}
.dates li.g{background:linear-gradient(90deg,var(--green),var(--green-soft))}
.dates li.b{background:linear-gradient(90deg,var(--band-a),var(--sky))}
.dates .d{flex:0 0 62px;padding-left:6px;font-size:9.4px;border-right:1.3px solid var(--white);line-height:12px}
.dates .t{padding:0 6px 0 6px;font-size:7.3px;line-height:8.6px}

/* sponsors */
.cosp{left:415px;top:1103px;width:330px;font-weight:700;font-size:9.9px;line-height:12px;color:#111}
.marks{left:415px;top:1143px;width:327px;display:flex;justify-content:space-between;align-items:center}
.mark{display:flex;align-items:center;gap:4px;font-weight:800;color:var(--navy-deep)}
.mark .sq{width:12px;height:12px;background:var(--navy-deep)}
.mark-a{font-size:9px;line-height:10px;width:90px}
.mark-b{font-size:16px}
.mark-c{font-size:18px}
</style>
</head>
<body>

<header class="hero abs">
  <svg width="777" height="216" viewBox="0 0 777 216" aria-hidden="true">
    <defs>
      <linearGradient id="heroGreen" x1="0" y1="1" x2="1" y2="0">
        <stop offset="0" stop-color="#6ec07a"/>
        <stop offset="1" stop-color="#6cc7ad"/>
      </linearGradient>
      <linearGradient id="heroBand" x1="0" y1="0" x2="1" y2="0">
        <stop offset="0" stop-color="#2cb9ee"/>
        <stop offset="1" stop-color="#3d58a6"/>
      </linearGradient>
    </defs>
    <polygon points="0,0 352,0 418,56 352,120 287,215 0,215" fill="url(#heroGreen)"/>
    <polygon points="357,0 396,0 455,56 372,126 381,112 425,56" fill="url(#heroGreen)"/>
    <polygon points="344,136 777,136 777,215 300,215" fill="url(#heroBand)"/>
  </svg>
  <div class="hero-title abs">CALL FOR PAPERS<br>&amp; PROPOSALS</div>
  <div class="hero-sub abs">oKTV 2021: 7th International<br>Conference of the Open<br>Knowledge Trails Venture</div>
  <div class="hero-theme abs">“TRANSCEND: Accelerating learner engagement in XR<br>across time, place, and space”</div>
  <div class="brand abs">
    <span class="brand-dot"></span>
    <span class="brand-name">Open Knowledge<br>Trails Venture</span>
  </div>
  <div class="venue abs">oKTV Virtual Campus, powered by MostraqO<br>May 17 to June 10, 2021</div>
  <p class="topics abs">Serious Games · 3D Collaboration · eSports · AI &amp; Machine Learning · Robotics · Digital Twins · Embodied Pedagogical Agents · Medical &amp; Healthcare Education · Workforce &amp; Industry · Cultural Heritage · Language Learning · K-12 STEM · Museums &amp; Libraries · Informal Learning · Community &amp; Civic Engagement · Special Education · Geosciences · Data Visualization and Analytics · Assessment &amp; Evaluation</p>
</header>

<section class="intro abs">
  <p>The 7th International Conference of the Open Knowledge Trails Venture (oKTV 2021) will be an innovative and interactive virtual gathering for a strengthening global network of researchers and practitioners collaborating to develop the scientific, technical, and applied potential of immersive learning. Held fully online and in virtual reality on the oKTV Virtual Campus, powered by MostraqO, it is the premier scholarly event focusing on advances in the use of virtual reality (VR), augmented reality (AR), mixed reality (MR), and other extended reality (XR) technologies to support learners across the full span of learning—from K-12 through higher education to work-based, informal, and lifelong learning contexts. Scholars and professionals working from informal and formal education settings as well as those representing diverse industry sectors are invited to participate in the conference, where they may share their research findings, experiences, and insights; network and establish partnerships to envision and shape the future of XR and immersive technologies for learning; and contribute to the emerging scholarly knowledge base on how these technologies can be used to create experiences that educate, engage, and excite learners.</p>
  <p class="note"><b>Note:</b> Last year’s oKTV conference drew over 3,600 attendees from across the globe, making the scheduling of sessions a challenge. This year’s conference activities will be spread over a four-week period so as to give attendees more opportunities to participate at times that are conducive to their local time zones.</p>
</section>

<div class="stream-tag abs">SUBMISSION STREAM</div>
<section class="stream s1 abs">
  <h3>Academic Stream</h3>
  <p>(Refereed paper published in proceedings)</p>
  <ul><li>Full (6–8 pages) paper for oral presentation</li><li>Short paper (4–5 pages) for oral presentation</li><li>Work-in-progress paper (2–3 pages) for poster presentation</li><li>Doctoral colloquium paper (2–3 pages)</li></ul>
</section>
<section class="stream s2 abs">
  <h3>Practitioner Stream</h3>
  <p>(No paper – Refereed on the basis of proposal form)</p>
  <ul><li>Oral presentation</li><li>Poster presentation</li><li>Guided virtual adventures</li><li>Immersive learning project showcase</li></ul>
</section>
<section class="stream s3 abs">
  <h3>Nontraditional Session Stream</h3>
  <p>(Extended abstract describing session published in proceedings)</p>
  <ul><li>Workshop</li><li>Special session</li><li>Panel session</li></ul>
</section>

<section class="panel tracks abs">
  <svg width="400" height="169" aria-hidden="true">
    <defs><linearGradient id="bandL" x1="0" y1="0" x2="1" y2="0"><stop offset="0" stop-color="#3a5aa8"/><stop offset="1" stop-color="#2bb8ec"/></linearGradient></defs>
    <polygon points="0,0 366,0 398,84 366,169 0,169" fill="url(#bandL)"/>
  </svg>
  <div class="inner">
    <h2>PROGRAM TRACKS</h2>
    <p>Papers and proposals may be submitted to one of six program tracks, administered by the nine oKTV Houses: Track 1. Early Childhood Development &amp; Learning (ECDL); Track 2. Galleries, Archives, Libraries, &amp; Museums (GLAM); Track 3. Inclusion, Diversity, Equity, Access, &amp; Social Justice (IDEAS); Track 4. K-12 STEM Education; Track 5. Language, Culture, &amp; Heritage (LCH); Track 6. Medical &amp; Healthcare Education (MHE); Track 7. Nature &amp; Environmental Sciences (NES); Track 8. Workforce Development &amp; Industry Training (WDIT); Track 9. Assessment and Evaluation (A&amp;E)</p>
  </div>
</section>

<section class="panel review abs">
  <svg width="400" height="168" aria-hidden="true">
    <polygon points="0,0 366,0 398,84 366,168 0,168" fill="url(#bandL)"/>
  </svg>
  <div class="inner">
    <h2>PAPER/PROPOSAL SUBMISSION AND REVIEW</h2>
    <p>Papers for the Academic Stream and extended-abstract proposals for the Nontraditional Session Stream must be prepared in standard UQTA double-column US Letter format using Wordsmith or TeXform, and will be accepted only via the online submission system, accessible via the conference website (from which guidelines and templates are also available).</p>
    <p>Proposals for the Practitioner Stream are to be submitted via an online form, also accessible from the conference website.</p>
    <p>A blind peer-review process will be used to evaluate all submissions.</p>
  </div>
</section>

<section class="panel pub abs">
  <svg width="408" height="182" aria-hidden="true">
    <defs><linearGradient id="bandR" x1="0" y1="0" x2="1" y2="0"><stop offset="0" stop-color="#2bb8ec"/><stop offset="1" stop-color="#3a5aa8"/></linearGradient></defs>
    <polygon points="34,0 408,0 408,182 34,182 0,91" fill="url(#bandR)"/>
  </svg>
  <div class="inner">
    <h2>PUBLICATION, ABSTRACTING, AND INDEXING</h2>
    <p>All accepted and registered papers in the Academic Stream that are presented at oKTV 2020 and all extended abstracts describing the Nontraditional Sessions presented at the conference will be published in the conference proceedings and submitted to the UQTA Vault® digital library. Content loaded into the Vault is made available by UQTA to its abstracting and indexing partners, including Verdane (Indexa, EngiDex), Luminar Analytics (CPRI—part of Web of Research) and others, for potential inclusion in their respective databases. In addition, authors of selected papers may be invited to submit expanded versions of their papers for consideration by a number of Indexa and Web of Research-indexed journals.</p>
  </div>
</section>

<section class="fmt abs">
  <h2>Session Format</h2>
  <ul>
    <li><svg width="15" height="15" viewBox="0 0 16 16" aria-hidden="true"><circle cx="8" cy="8" r="6.8" fill="none" stroke="#1ba865" stroke-width="1.5"/><path d="M4.6 8.2l2.4 2.4 5-5.6" fill="none" stroke="#1ba865" stroke-width="1.8"/></svg><span><b>Oral presentation:</b> Pre-recorded video + 60-minute live in-world discussion with others presenting on similar/related topics (groupings of presenters into sessions determined by Program Committee)</span></li>
    <li><svg width="15" height="15" viewBox="0 0 16 16" aria-hidden="true"><circle cx="8" cy="8" r="6.8" fill="none" stroke="#1ba865" stroke-width="1.5"/><path d="M4.6 8.2l2.4 2.4 5-5.6" fill="none" stroke="#1ba865" stroke-width="1.8"/></svg><span><b>Poster presentation:</b> Live poster session in 3D virtual exhibition hall; pre-recorded video optional</span></li>
    <li><svg width="15" height="15" viewBox="0 0 16 16" aria-hidden="true"><circle cx="8" cy="8" r="6.8" fill="none" stroke="#1ba865" stroke-width="1.5"/><path d="M4.6 8.2l2.4 2.4 5-5.6" fill="none" stroke="#1ba865" stroke-width="1.8"/></svg><span><b>Doctoral colloquium:</b> 60-minute live in-world discussion with other doctoral researchers; pre-recorded video optional</span></li>
    <li><svg width="15" height="15" viewBox="0 0 16 16" aria-hidden="true"><circle cx="8" cy="8" r="6.8" fill="none" stroke="#1ba865" stroke-width="1.5"/><path d="M4.6 8.2l2.4 2.4 5-5.6" fill="none" stroke="#1ba865" stroke-width="1.8"/></svg><span><b>Guided virtual adventures:</b> 60-minute small-group guided tours of to various social and collaborative XR/immersive environments and platforms</span></li>
    <li><svg width="15" height="15" viewBox="0 0 16 16" aria-hidden="true"><circle cx="8" cy="8" r="6.8" fill="none" stroke="#1ba865" stroke-width="1.5"/><path d="M4.6 8.2l2.4 2.4 5-5.6" fill="none" stroke="#1ba865" stroke-width="1.8"/></svg><span><b>Immersive learning project showcase:</b> WebXR space to assemble a collection of virtual artifacts, accessible to attendees throughout the conference</span></li>
    <li><svg width="15" height="15" viewBox="0 0 16 16" aria-hidden="true"><circle cx="8" cy="8" r="6.8" fill="none" stroke="#1ba865" stroke-width="1.5"/><path d="M4.6 8.2l2.4 2.4 5-5.6" fill="none" stroke="#1ba865" stroke-width="1.8"/></svg><span><b>Special session:</b> 30- or 60-minute live interactive session held in world; may optionally be linked to one or more papers</span></li>
    <li><svg width="15" height="15" viewBox="0 0 16 16" aria-hidden="true"><circle cx="8" cy="8" r="6.8" fill="none" stroke="#1ba865" stroke-width="1.5"/><path d="M4.6 8.2l2.4 2.4 5-5.6" fill="none" stroke="#1ba865" stroke-width="1.8"/></svg><span><b>Panel session:</b> 60-minute live in-world discussion with a self-formed group of 3-5 panelists (including a lead panelist who serves as a moderator)</span></li>
  </ul>
</section>

<div class="dates-title abs">IMPORTANT DATES</div>
<ul class="dates abs">
  <li class="g"><span class="d">2020-12-11</span><span class="t">Paper and proposal submission deadline (Main round – all submission types welcome)</span></li>
  <li class="b"><span class="d">2021-03-01</span><span class="t">Notification of review outcomes from main submission round</span></li>
  <li class="g"><span class="d">2021-03-15</span><span class="t">Camera-ready papers for proceedings due – Full and short papers</span></li>
  <li class="b"><span class="d">2021-03-15</span><span class="t">Presenter registration deadline – Full and short papers</span></li>
  <li class="g"><span class="d">2021-03-08</span><span class="t">Paper and proposal submission deadline (Late round – Only work-in-progress papers, nontraditional session proposals, and practitioner proposals will be considered*)</span></li>
  <li class="b"><span class="d">2021-04-19</span><span class="t">Notification of review outcomes from late submission round</span></li>
  <li class="g"><span class="d">2021-05-03</span><span class="t">Camera-ready work-in-progress papers and nontraditional session extended abstracts for proceedings due; final practitioner abstracts for conference program due</span></li>
  <li class="b"><span class="d">2021-05-03</span><span class="t">Presenter registration deadline – Work-in-progress papers, practitioner sessions, and nontraditional sessions</span></li>
  <li class="g"><span class="d">2020-05-10</span><span class="t">Deadline for uploading presentation materials (videos, slides for oral presentations, posters for poster presentations)</span></li>
  <li class="b"><span class="d">2020-05-17</span><span class="t">Conference opening</span></li>
</ul>

<p class="cosp abs">Technically co-sponsored by the UQTA Learning Society, with proceedings to be submitted for inclusion in UQTA Vault®</p>
<div class="marks abs">
  <span class="mark mark-a">UQTA Learning Society</span>
  <span class="mark mark-b">MostraqO</span>
  <span class="mark mark-c"><span class="sq"></span>UQTA</span>
</div>

</body>
</html>
```